Harbor Kindness Fund - New Website Design

I need a site that looks like this http://wheelgift-relief.org for boat donations. So please replace the cars with boats.

```html
<!DOCTYPE html>
<html lang="en">
<head>
<meta charset="utf-8">
<title>Harbor Kindness Fund – Donate Your Boat</title>
<link href="https://fonts.googleapis.com/css2?family=Roboto:wght@300;400;500;700&display=swap" rel="stylesheet">
<style>
:root{
  --blue:#4a6cb3;
  --blue-dark:#3d5c9e;
  --coral:#f26b5b;
  --coral-soft:#f7897c;
  --cream:#fdf6e4;
  --pink:#fde4e2;
  --ink:#333a44;
  --muted:#6b6f76;
  --rule:#e3e3e3;
  --white:#ffffff;
}
*{box-sizing:border-box;margin:0;padding:0}
html,body{width:1200px;height:4412px;overflow:hidden}
body{font-family:'Roboto',Arial,sans-serif;color:var(--ink);background:var(--white);position:relative}
section,header,footer{position:absolute;left:0;width:1200px}
.section-title{text-align:center;font-weight:400;font-size:34px;color:var(--blue)}
.divider{display:block;margin:14px auto 0;width:40px;height:8px}
.btn{display:inline-block;background:var(--blue);color:var(--white);font-size:16px;padding:12px 38px;text-decoration:none}
.art{position:absolute}

/* header */
.site-header{top:0;height:118px;background:var(--white)}
.brand{position:absolute;left:80px;top:30px;display:flex;align-items:center;gap:14px}
.brand-mark{width:44px;height:44px;border-radius:50%;background:var(--coral)}
.brand-name{font-size:22px;font-weight:500;color:var(--blue);line-height:1.1;width:200px}
.call{position:absolute;left:664px;top:44px;font-size:22px;font-weight:500;color:var(--ink);display:flex;align-items:center;gap:10px}
.call svg{width:36px;height:36px}
.header-donate{position:absolute;left:954px;top:44px;padding:9px 30px;font-size:18px}

/* hero */
.hero{top:118px;height:587px;background:linear-gradient(100deg,#d9eaea 0%,#e9d7cc 35%,#f4eee8 60%,#f6f2ee 100%)}
.hero-photo{left:0;top:0;width:560px;height:587px;background:radial-gradient(ellipse at 45% 40%,#f1cdb8 0%,#9fd0cc 45%,#cfe3e2 80%);}
.hero-curve{position:absolute;left:0;top:-2px;width:1200px;height:40px}
.hero-copy{position:absolute;left:440px;top:262px;width:250px;text-align:right}
.hero-copy h1{font-size:34px;font-weight:400;color:var(--blue);line-height:1.25}
.hero-copy p{font-size:18px;color:var(--coral);margin-top:10px}
.pickup-form{position:absolute;left:700px;top:0;width:500px;height:427px;background:var(--blue);padding:0 48px;color:var(--white)}
.pickup-form h2{text-align:center;font-size:26px;font-weight:400;padding:14px 0 12px;border-bottom:1px solid rgba(255,255,255,.35);margin:0 -48px 14px}
.pickup-form h3{font-size:16px;font-weight:500;margin:10px 0 10px}
.field-row{display:flex;gap:14px;margin-bottom:12px}
.field{flex:1;height:38px;background:var(--white);color:#9aa0a8;font-size:13px;line-height:38px;padding-left:14px}
.submit{display:block;width:210px;margin:14px auto 0;background:var(--coral);text-align:center;font-size:17px;padding:9px 0}
.hero-bottom{position:absolute;left:0;bottom:0;width:1200px;height:6px;background:var(--coral-soft)}

/* welcome */
.welcome{top:705px;height:605px;background:var(--cream);text-align:center}
.welcome .section-title{margin-top:58px}
.welcome p{font-size:14px;color:var(--ink);line-height:1.5;margin-top:30px}
.welcome p + p{margin-top:20px}
.welcome .btn{margin-top:38px}
.kids{left:330px;top:340px;width:540px;height:215px;border-radius:40px;background:linear-gradient(90deg,#f7c37a,#8fc4e8,#f4a6a0,#f7d774,#e79bb8)}

/* features */
.features{top:1310px;height:425px}
.features .section-title{margin-top:54px}
.feature-list{position:absolute;left:84px;top:190px;width:1032px;display:flex;justify-content:space-between}
.feature{width:180px;text-align:center}
.feature svg{width:52px;height:52px}
.feature h3{font-size:16px;font-weight:500;margin-top:12px;line-height:1.3}
.feature p{font-size:12.5px;color:var(--muted);line-height:1.5;margin-top:12px}

/* donate today */
.donate-today{top:1735px;height:523px;background:linear-gradient(90deg,#efe6df 0%,#e7d5c6 40%,#f3ece4 70%,#ece5dc 100%)}
.donate-photo{left:0;top:0;width:1200px;height:523px;background:radial-gradient(ellipse at 78% 45%,#f5d8c2 0%,#e9ddd0 30%,rgba(240,233,226,0) 60%),linear-gradient(90deg,#f0e8e0,#d9c3ae 45%,#efe7dd 65%,#e6ddd0)}
.donate-copy{position:absolute;left:80px;top:88px;width:490px}
.donate-copy h2{font-size:34px;font-weight:400;color:var(--blue)}
.donate-copy p{font-size:17px;line-height:1.45;margin-top:22px;color:var(--ink)}
.donate-copy p.small{font-size:14px;margin-top:14px;color:var(--muted)}
.donate-copy .btn{margin-top:22px;padding:10px 36px;font-size:15px}

/* why */
.why{top:2258px;height:742px}
.why .section-title{margin-top:60px}
.why-center{left:470px;top:315px;width:260px;height:230px;border-radius:50%;background:radial-gradient(circle,#f0736a 0%,#f7c36f 55%,#ffffff 72%)}
.reason{position:absolute;width:330px;display:flex;align-items:center;gap:14px}
.reason.left{text-align:right}
.reason h3{font-size:16px;font-weight:700;color:var(--ink)}
.reason p{font-size:12px;color:var(--ink);line-height:1.45;margin-top:4px}
.badge{flex:none;width:64px;height:64px;border-radius:50%;background:var(--coral);display:flex;align-items:center;justify-content:center}
.badge svg{width:32px;height:32px}
.reason.centered{flex-direction:row;text-align:center}

/* how */
.how{top:3000px;height:470px;background:var(--pink)}
.how .section-title{margin-top:54px}
.steps{position:absolute;left:80px;top:190px;width:1040px;display:flex;justify-content:space-between}
.step{width:300px;text-align:center}
.step-art{width:158px;height:158px;border-radius:50%;margin:0 auto}
.step h3{font-size:18px;font-weight:400;margin-top:24px}
.step p{font-size:12.5px;color:var(--muted);line-height:1.5;margin-top:14px}

/* faq */
.faq{top:3470px;height:550px}
.faq .section-title{margin-top:68px}
.faq-list{position:absolute;left:80px;top:176px;width:650px;list-style:none}
.faq-item{display:flex;border-bottom:2px solid var(--white);background:#eef1f7;font-size:14px}
.faq-q{flex:none;width:34px;background:var(--blue);color:var(--white);text-align:center;line-height:34px}
.faq-text{padding:0 14px;line-height:34px;color:var(--ink)}
.faq-item.open{background:var(--blue);color:var(--white)}
.faq-item.open .faq-q{background:var(--blue-dark)}
.faq-item.open .faq-text{color:var(--white)}
.faq-answer{font-size:12.5px;line-height:1.5;padding:0 14px 14px;opacity:.9}
.faq-art{left:800px;top:210px;width:230px;height:250px;border-radius:50% 50% 40% 40%;background:radial-gradient(circle at 40% 30%,#ee4a5d 0%,#f7a86f 45%,#fff 72%)}

/* footer */
.site-footer{top:4020px;height:337px;background:linear-gradient(90deg,#f26b5b,#f47e6d 50%,#f26b5b);color:var(--white)}
.footer-col{position:absolute;top:62px}
.footer-col h4{font-size:20px;font-weight:400;padding-bottom:10px;border-bottom:1px solid rgba(255,255,255,.4)}
.footer-col ul{list-style:none;margin-top:14px}
.footer-col li{font-size:14px;line-height:1.7;display:flex;align-items:center;gap:8px}
.footer-col p{font-size:13px;line-height:1.5;margin-top:14px}
.sub-row{display:flex;margin-top:12px}
.sub-input{width:170px;height:26px;background:var(--white);color:#999;font-size:12px;line-height:26px;padding-left:8px}
.sub-btn{display:inline-block;margin-top:8px;background:var(--blue);font-size:12px;padding:5px 10px}
.social-dot{width:20px;height:20px;background:var(--blue)}
.copyright{top:4357px;height:55px;background:var(--blue);color:var(--white);font-size:13px}
.copyright span{position:absolute;left:80px;top:19px}
.trust{position:absolute;top:10px;width:52px;height:36px;background:var(--white);border-radius:4px}
</style>
</head>
<body>

<header class="site-header">
  <div class="brand"><span class="brand-mark"></span><span class="brand-name">Harbor Kindness Fund</span></div>
  <div class="call">
    <svg viewBox="0 0 36 36"><circle cx="18" cy="18" r="16" fill="none" stroke="#f26b5b" stroke-width="2"/><path d="M12 10l4 0 1 5-2 2c1 2 3 4 5 5l2-2 5 1 0 4c-8 1-16-7-15-15z" fill="#f26b5b"/></svg>
    Call : 1-800-555-0142
  </div>
  <a class="btn header-donate">Donate Now</a>
</header>

<section class="hero">
  <div class="art hero-photo" role="img" aria-label="Photo of a smiling child wearing a headscarf"></div>
  <svg class="hero-curve" viewBox="0 0 1200 40" preserveAspectRatio="none"><path d="M0 0 L1200 0 L1200 18 Q600 44 0 18 Z" fill="#f7897c"/><path d="M0 0 L1200 0 L1200 10 Q600 34 0 10 Z" fill="#ffffff"/></svg>
  <div class="hero-copy">
    <h1>Donate Boat To Charity!</h1>
    <p>Your Boat Can Make A Difference!</p>
  </div>
  <form class="pickup-form">
    <h2>Donation Pick Up Form</h2>
    <h3>Contact Information:</h3>
    <div class="field-row"><div class="field">First Name</div><div class="field">Last Name</div></div>
    <div class="field-row"><div class="field">Email Address</div></div>
    <h3>Auto Donation Information:</h3>
    <div class="field-row"><div class="field">Choose Year</div><div class="field">Choose Make</div></div>
    <div class="field-row"><div class="field">Model Of Vehicle</div></div>
    <div class="submit">Submit Application</div>
  </form>
  <div class="hero-bottom"></div>
</section>

<section class="welcome">
  <h2 class="section-title">Welcome To HKF</h2>
  <svg class="divider" viewBox="0 0 40 8"><line x1="0" y1="4" x2="40" y2="4" stroke="#f26b5b"/><circle cx="14" cy="4" r="3" fill="#f26b5b"/><circle cx="26" cy="4" r="3" fill="#f26b5b"/></svg>
  <p><strong>Harbor Kindness Fund</strong>'s mission is to improve, empower and to bring joy to the lives of children and their families affected by cancer.</p>
  <p>HKF adapts its support to fit each child's needs, from education to assistance with treatment, recovery and family support.</p>
  <a class="btn">Read More</a>
  <div class="art kids" role="img" aria-label="Illustration of five cheerful children jumping"></div>
</section>

<section class="features">
  <h2 class="section-title">Donate Your Boats To Charity &amp; Make a Difference</h2>
  <svg class="divider" viewBox="0 0 40 8"><line x1="0" y1="4" x2="40" y2="4" stroke="#f26b5b"/><circle cx="14" cy="4" r="3" fill="#f26b5b"/><circle cx="26" cy="4" r="3" fill="#f26b5b"/></svg>
  <div class="feature-list">
    <div class="feature"><svg viewBox="0 0 52 52"><circle cx="26" cy="26" r="20" fill="none" stroke="#f26b5b" stroke-width="3"/><text x="26" y="33" text-anchor="middle" font-size="20" fill="#4a6cb3" font-family="Roboto,sans-serif">$</text></svg><h3>You Have<br>No Costs</h3><p>Maecenas rutrum auctor diam. In et pellentesque sapien. Orci varius natoque penatibus.</p></div>
    <div class="feature"><svg viewBox="0 0 52 52"><rect x="4" y="20" width="26" height="16" fill="#f26b5b"/><path d="M30 24h10l6 6v6H30z" fill="#4a6cb3"/><circle cx="13" cy="40" r="5" fill="#4a6cb3"/><circle cx="38" cy="40" r="5" fill="#4a6cb3"/></svg><h3>Free Towing,<br>Running Or Not</h3><p>Maecenas rutrum auctor diam. In et pellentesque sapien. Orci varius natoque penatibus.</p></div>
    <div class="feature"><svg viewBox="0 0 52 52"><rect x="12" y="6" width="28" height="40" rx="2" fill="none" stroke="#f26b5b" stroke-width="3"/><line x1="18" y1="18" x2="34" y2="18" stroke="#4a6cb3" stroke-width="3"/><line x1="18" y1="26" x2="34" y2="26" stroke="#4a6cb3" stroke-width="3"/><line x1="18" y1="34" x2="28" y2="34" stroke="#4a6cb3" stroke-width="3"/></svg><h3>We Issue You An<br>IRS Tax Receipt</h3><p>Maecenas rutrum auctor diam. In et pellentesque sapien. Orci varius natoque penatibus.</p></div>
    <div class="feature"><svg viewBox="0 0 52 52"><rect x="10" y="8" width="28" height="38" fill="none" stroke="#f26b5b" stroke-width="3"/><path d="M30 30l12-16 4 3-12 16-5 2z" fill="#4a6cb3"/></svg><h3>We Take Care Of<br>All Paperwork</h3><p>Maecenas rutrum auctor diam. In et pellentesque sapien. Orci varius natoque penatibus.</p></div>
    <div class="feature"><svg viewBox="0 0 52 52"><rect x="12" y="8" width="28" height="38" rx="2" fill="none" stroke="#f26b5b" stroke-width="3"/><path d="M18 26l5 5 10-11" fill="none" stroke="#4a6cb3" stroke-width="3"/></svg><h3>We Take Care Of<br>DMV &amp; Smog Issues</h3><p>Maecenas rutrum auctor diam. In et pellentesque sapien. Orci varius natoque penatibus.</p></div>
  </div>
</section>

<section class="donate-today">
  <div class="art donate-photo" role="img" aria-label="Photo of a happy child in a bright room with potted plants"></div>
  <div class="donate-copy">
    <h2>Donate Your Boat Today!</h2>
    <p>Vivamus id est at nunc tempor lacinia. Donec sed mi hendrerit sapien aliquet euismod. Quisque fringilla metus sed sapien mollis, quis pellentesque augue rutrum.</p>
    <p class="small">Ut non tincidunt nisi. Vestibulum ante ipsum primis in faucibus orci luctus et ultrices posuere cubilia Curae; Aliquam ultrices tempus magna ac imperdiet.</p>
    <a class="btn">Donate Now</a>
  </div>
</section>

<section class="why">
  <h2 class="section-title">Why Donate Your Boats To Us</h2>
  <svg class="divider" viewBox="0 0 40 8"><line x1="0" y1="4" x2="40" y2="4" stroke="#f26b5b"/><circle cx="14" cy="4" r="3" fill="#f26b5b"/><circle cx="26" cy="4" r="3" fill="#f26b5b"/></svg>
  <div class="art why-center" role="img" aria-label="Illustration of two children riding in a small red boat"></div>

  <div class="reason left" style="left:220px;top:180px"><div><h3>IRS 501(c)3 Approved:</h3><p>Free 24/7 Pickup with No DMV Hassles.</p></div><span class="badge"><svg viewBox="0 0 32 32"><path d="M7 17l6 6 12-14" fill="none" stroke="#fff" stroke-width="3"/></svg></span></div>
  <div class="reason" style="left:630px;top:180px"><span class="badge"><svg viewBox="0 0 32 32"><rect x="8" y="5" width="16" height="22" fill="none" stroke="#fff" stroke-width="2.5"/><line x1="12" y1="12" x2="20" y2="12" stroke="#fff" stroke-width="2"/><line x1="12" y1="18" x2="20" y2="18" stroke="#fff" stroke-width="2"/></svg></span><div><h3>Income Tax Deduction:</h3><p>We issue you an IRS tax receipt &amp; offer the largest resale network to get you the highest tax write-off possible.</p></div></div>

  <div class="reason left" style="left:90px;top:320px"><div><h3>Free Local Towing to You:</h3><p>We will pick up your boat donation, running or not, when it's most convenient, at home or work.</p></div><span class="badge"><svg viewBox="0 0 32 32"><rect x="4" y="13" width="16" height="9" fill="#fff"/><path d="M20 15h5l4 4v3h-9z" fill="#fff"/><circle cx="10" cy="25" r="3" fill="#fff"/><circle cx="24" cy="25" r="3" fill="#fff"/></svg></span></div>
  <div class="reason" style="left:780px;top:320px"><span class="badge"><svg viewBox="0 0 32 32"><rect x="8" y="5" width="16" height="22" fill="none" stroke="#fff" stroke-width="2.5"/><line x1="6" y1="26" x2="26" y2="6" stroke="#fff" stroke-width="2.5"/></svg></span><div><h3>No Paperwork Hassles:</h3><p>We take any boat and handle everything DMV, Smog and IRS paperwork.</p></div></div>

  <div class="reason left" style="left:90px;top:480px"><div><h3>All Boats Accepted:</h3><p>We take your boat regardless of its condition or registration status.</p></div><span class="badge"><svg viewBox="0 0 32 32"><path d="M4 18h24l-4 7H8z" fill="#fff"/><path d="M15 5v12h-8z" fill="#fff"/></svg></span></div>
  <div class="reason" style="left:780px;top:480px"><span class="badge"><svg viewBox="0 0 32 32"><circle cx="16" cy="16" r="9" fill="none" stroke="#fff" stroke-width="2.5"/><text x="16" y="21" text-anchor="middle" font-size="13" fill="#fff" font-family="Roboto,sans-serif">$</text></svg></span><div><h3>Boat donations help fund programs:</h3><p>And benefit Coastal Family Support Fund. An IRS 501(c)3 nonprofit organization.</p></div></div>

  <div class="reason left" style="left:410px;top:585px;width:370px"><div><h3>Schedule a Free Pickup:</h3><p>Complete the form and a representative will call you to arrange a convenient time to pickup your boat.</p></div><span class="badge"><svg viewBox="0 0 32 32"><rect x="5" y="8" width="22" height="19" fill="none" stroke="#fff" stroke-width="2.5"/><line x1="5" y1="14" x2="27" y2="14" stroke="#fff" stroke-width="2"/></svg></span></div>
</section>

<section class="how">
  <h2 class="section-title">How It Works</h2>
  <svg class="divider" viewBox="0 0 40 8"><line x1="0" y1="4" x2="40" y2="4" stroke="#f26b5b"/><circle cx="14" cy="4" r="3" fill="#f26b5b"/><circle cx="26" cy="4" r="3" fill="#f26b5b"/></svg>
  <div class="steps">
    <div class="step"><div class="step-art" role="img" aria-label="Illustration of a checklist form" style="background:radial-gradient(circle,#e9f3ea 0%,#2fa78a 62%)"></div><h3>1. Fill Out The Simple Form</h3><p>Lorem ipsum dolor sit amet, consectetur adipiscing elit. Cras at odio ligula. Quisque commodo mauris ex, ac maximus eros consequat eu.</p></div>
    <div class="step"><div class="step-art" role="img" aria-label="Illustration of a tow truck pulling a boat" style="background:radial-gradient(circle,#f3c2bd 0%,#e9e7ee 62%)"></div><h3>2. Schedule Your Free Pick-up</h3><p>Lorem ipsum dolor sit amet, consectetur adipiscing elit. Cras at odio ligula. Quisque commodo mauris ex, ac maximus eros consequat eu.</p></div>
    <div class="step"><div class="step-art" role="img" aria-label="Illustration of a tax document with a red tag" style="background:radial-gradient(circle,#e8503f 0%,#3aa08f 62%)"></div><h3>3. Receive Tax Deduction</h3><p>Lorem ipsum dolor sit amet, consectetur adipiscing elit. Cras at odio ligula. Quisque commodo mauris ex, ac maximus eros consequat eu.</p></div>
  </div>
</section>

<section class="faq">
  <h2 class="section-title">FAQs</h2>
  <svg class="divider" viewBox="0 0 40 8"><line x1="0" y1="4" x2="40" y2="4" stroke="#f26b5b"/><circle cx="14" cy="4" r="3" fill="#f26b5b"/><circle cx="26" cy="4" r="3" fill="#f26b5b"/></svg>
  <ul class="faq-list">
    <li class="faq-item"><span class="faq-q">Q</span><span class="faq-text">What types of vehicles can be donated?</span></li>
    <li class="faq-item open"><span class="faq-q">Q</span><div><div class="faq-text">What paperwork do I need to donate my vehicle?</div><p class="faq-answer">All you need is a title, free of all liens. We will request some general information from you at the time of donation such as the year, make, and model of the boat as well as its general mechanical condition. We accept all vehicles, running or non-running.</p></div></li>
    <li class="faq-item"><span class="faq-q">Q</span><span class="faq-text">Is my donated vehicle tax deductible?</span></li>
    <li class="faq-item"><span class="faq-q">Q</span><span class="faq-text">What if the vehicle is not registered in my name?</span></li>
    <li class="faq-item"><span class="faq-q">Q</span><span class="faq-text">How much will I receive as a tax deduction for my vehicle?</span></li>
    <li class="faq-item"><span class="faq-q">Q</span><span class="faq-text">When will I receive my tax receipt?</span></li>
    <li class="faq-item"><span class="faq-q">Q</span><span class="faq-text">How do I schedule a pick up?</span></li>
  </ul>
  <div class="art faq-art" role="img" aria-label="Illustration of a puppy and kitten holding heart balloons"></div>
</section>

<footer class="site-footer">
  <div class="footer-col" style="left:80px;width:190px">
    <h4>Quick Links</h4>
    <ul><li>› Home</li><li>› About us</li><li>› How It Works</li><li>› Why Donate</li><li>› FAQs</li><li>› Contact Us</li></ul>
  </div>
  <div class="footer-col" style="left:303px;width:260px">
    <h4>Contact Information</h4>
    <ul>
      <li><svg width="14" height="16" viewBox="0 0 14 16"><path d="M7 0a6 6 0 0 0-6 6c0 4 6 10 6 10s6-6 6-10a6 6 0 0 0-6-6z" fill="#fff"/><circle cx="7" cy="6" r="2" fill="#f26b5b"/></svg>18 Pier Lane, Bayport</li>
      <li><svg width="14" height="14" viewBox="0 0 14 14"><path d="M2 1h3l1 3-2 1c1 2 2 3 4 4l1-2 3 1v3C6 12 1 7 2 1z" fill="#fff"/></svg>1-800-555-0177</li>
    </ul>
  </div>
  <div class="footer-col" style="left:640px;width:220px">
    <h4>Newsletter Signup</h4>
    <p>Please enter your email address below to receive our FREE newsletter.</p>
    <div class="sub-row"><div class="sub-input">Your Email ID</div></div>
    <span class="sub-btn">Subscribe</span>
  </div>
  <div class="footer-col" style="left:932px;width:190px">
    <h4>Follow Us</h4>
    <ul><li><span class="social-dot"></span>Community Page</li><li><span class="social-dot"></span>Professional Network</li><li><span class="social-dot"></span>Short Updates</li><li><span class="social-dot"></span>Email</li></ul>
  </div>
</footer>

<div class="copyright" style="position:absolute;left:0;top:4357px;width:1200px">
  <span>Copyright © 2017, Harbor Kindness Fund. All Rights Are Reserved.</span>
  <div class="trust" style="left:996px"></div>
  <div class="trust" style="left:1060px"></div>
</div>

</body>
</html>
```